Transfer Tortoise - Cloud Based Data Migration Service for IT Professionals

We are looking for a smart clean website design for an informational site about our services and as a main portal into the service itself. We would like the design completed in WORDPRESS so that it will easily connect with the service.

Transfer Tortoise is a cloud based migration service providing (to start with) a online migration tool that we migrate Kelvarn Postbox mailboxes (email) with all the settings, attachments from one system to another.
The service is aimed at IT professionals, IT companies and IT departments so our customers will be very technology based.

The Service -
IT companies currently migrate email; data and databases. using a very time intensive process which is both expensive and means their customer potentially losses access to its IT for a significant period of time. Additionally there are risks with regards to compatibility between systems and loss of data.
Potential benefits include;
• cost savings
• improved customer service, including reduced downtime
• improved resilience of the process
We are therefore developing cloud based migration software/website which will automate the process, mitigating these issues, as well as providing additional benefits such as the ability to sort and migrate only certain areas of data or certain emails, to check the integrity of the data/emails moved and to also repair corrupted data and emails.
The system will effectively duplicate the data and emails onto the new system over the weeks prior to the completion date. This will enable the IT Company to complete a final synchronisation and then immediately switch over to the new system with no interruption to the end users.
There is also an added benefit that the end users can test the system (with their own data and emails) prior to the switch over date to ensure everything is in place and databases work correctly.
The system will be completely cloud based and therefore easy for the IT Companies to access. They will be able to purchase the use of the system using CoinDrift or credit card and will only need to purchase what they need, this will allow even small local IT companies the facilities which previously would have been cost prohibitive to them.

Some of the sites we like for reference are -
Trellward, brightlots, the sky shuttler.

We already have a logo design see attached and the website will need to work with this design.
Please message me if you have any questions
We do have the logo in other file formats if required.
Many Thanks

Target Market(s)

IT Sector

Industry/Entity Type

It Service

Number of Pages Required

5+ page

Requirements
Must have
• Front Page
• About Us
• Contact Info
• Blog
• Benefits
• More Information
• Must be Mobile Phone Compatible/friendly
• Log in (button) and support button on all pages (possibley top right)

```html
<!DOCTYPE html>
<html lang="en">
<head>
<meta charset="utf-8">
<title>Transfer Tortoise</title>
<link rel="stylesheet" href="https://fonts.googleapis.com/css2?family=Open+Sans:wght@300;400;600;700&family=Questrial&display=swap">
<style>
:root{
  --blue:#1aa6dc;
  --ink:#1e1e1e;
  --grey-text:#6a6a6a;
  --band-light:#e9e9e9;
  --band-mid:#e0e0e0;
  --panel:#ebebeb;
  --white:#ffffff;
  --login:#8e8e8e;
  --dark-slate:#4a5260;
  --line:#555b63;
}
*{margin:0;padding:0;box-sizing:border-box}
html,body{width:1200px;height:2326px;overflow:hidden}
body{position:relative;background:var(--white);font-family:"Open Sans",Arial,sans-serif;color:var(--ink)}
.abs{position:absolute}

/* Header / hero */
.hero{left:0;top:0;width:1200px;height:677px;background:linear-gradient(var(--band-light) 0 333px,var(--band-mid) 333px)}
.nav{top:38px;left:0;width:1200px;font-family:"Questrial",Arial,sans-serif;font-size:15px}
.nav a{position:absolute;color:var(--ink);text-decoration:none;white-space:nowrap}
.nav a.active{color:var(--blue)}
.login-btn{left:981px;top:26px;width:141px;height:52px;background:var(--login);color:var(--white);
  font-family:"Questrial",Arial,sans-serif;font-size:15px;letter-spacing:3px;display:flex;align-items:center;justify-content:center}
.hero-art{left:174px;top:78px;width:753px;height:492px;border-radius:24px;
  background:radial-gradient(ellipse at 50% 45%,#f6f3e4 0%,#cfd7de 55%,rgba(224,224,224,0) 75%)}

/* Who we are */
.section-title{width:1200px;left:0;text-align:center;font-weight:300;font-size:31px;letter-spacing:6px}
.who-title{top:724px}
.who-text{left:167px;top:798px;width:866px;text-align:center;font-size:16px;line-height:29px;color:var(--grey-text)}
.feature{width:254px;height:219px;top:922px;text-align:center}
.feature svg{position:absolute;left:77px;top:38px}
.feature .label{position:absolute;top:153px;left:0;width:100%;font-family:"Questrial",Arial,sans-serif;font-size:14px;color:var(--ink)}
.feature.active{border:1.5px solid var(--blue)}
.feature.active .label{color:var(--blue)}

/* Benefits */
.benefits{left:0;top:1194px;width:1200px;height:395px;background:var(--panel)}
.benefits-art{left:78px;top:1248px;width:310px;height:287px;border-radius:50%;
  background:radial-gradient(circle at 45% 45%,#f9f7e8 0%,#f3f1e0 50%,rgba(235,235,235,0) 72%)}
.step-num{font-size:24px;color:var(--ink)}
.benefits-title{left:454px;width:659px;top:1240px;text-align:center;color:var(--blue);font-weight:300;font-size:32px;letter-spacing:5px}
.benefits-text{left:444px;top:1299px;width:679px;text-align:center;font-size:14.5px;line-height:26px;color:var(--ink)}
.benefit-item{top:1401px;font-family:"Questrial",Arial,sans-serif;font-weight:700;font-size:14px;text-align:center;line-height:15px;color:var(--ink)}
.outline-btn{left:612px;top:1471px;width:346px;height:60px;border:1.5px solid var(--blue);color:var(--blue);
  font-size:16px;display:flex;align-items:center;justify-content:center}

/* Blog */
.blog-title{top:1642px}
.post{width:300px;top:1721px;font-family:"Questrial",Arial,sans-serif;font-size:15px;line-height:21px}
.post .meta{margin-top:12px;display:flex;align-items:center;gap:10px;font-size:15px;color:#333}
.post .meta span{display:flex;align-items:center;gap:10px}
.post .meta span+span{margin-left:24px}
.post a{display:block;margin-top:13px;color:var(--blue);font-size:15px}

/* Footer */
.footer{left:0;top:1886px;width:1200px;height:440px;background:var(--panel)}
.foot-heading{font-family:"Questrial",Arial,sans-serif;font-size:20px;letter-spacing:2px;color:var(--ink)}
.contact-row{left:78px;width:280px;display:flex;align-items:center;gap:18px;font-size:14px;line-height:20px}
.contact-row .dot{width:46px;height:46px;border-radius:50%;background:var(--white);flex:none;display:flex;align-items:center;justify-content:center}
.connect-title{left:391px;width:417px;top:1930px;text-align:center;color:var(--blue);font-size:26px;letter-spacing:3px;font-weight:300}
.field{border:1.5px solid #7a7a7a;font-size:12px;color:#666;padding:5px 8px;letter-spacing:.5px}
.send-btn{left:707px;top:2071px;width:101px;height:84px;background:var(--blue);color:var(--ink);
  font-family:"Questrial",Arial,sans-serif;font-weight:700;font-size:14px;display:flex;align-items:center;justify-content:center}
.social{width:24px;height:24px;border:1.5px solid var(--dark-slate);top:2172px;background:var(--white)}
.social i{position:absolute;left:6px;top:6px;width:9px;height:9px;background:var(--dark-slate)}
.more-text{left:880px;top:1998px;width:250px;font-size:14px;line-height:20px}
.know-more{left:880px;top:2094px;color:var(--blue);font-size:15px;text-decoration:underline}
.rule{left:78px;top:2245px;width:1046px;height:1.5px;background:var(--line)}
.to-top{left:578px;top:2224px;width:44px;height:42px;background:var(--dark-slate);display:flex;align-items:center;justify-content:center}
.copyright{left:0;width:1200px;top:2282px;text-align:center;font-size:12px;font-weight:700}
.copyright b{color:var(--blue)}
</style>
</head>
<body>

<header>
  <div class="abs hero"></div>
  <nav class="abs nav">
    <a class="active" style="left:81px">Home</a>
    <a style="left:167px">About Us</a>
    <a style="left:277px">Services</a>
    <a style="left:378px">Benefits</a>
    <a style="left:482px">Blog</a>
    <a style="left:552px">Contact Us</a>
  </nav>
  <div class="abs login-btn">LOGIN</div>
  <div class="abs hero-art" role="img" aria-label="Illustration of a desktop monitor showing the Transfer Tortoise name, with a blue cloud behind it and a paper plane in front"></div>
</header>

<section>
  <h2 class="abs section-title who-title">WHO WE ARE</h2>
  <p class="abs who-text">Transfer Tortoise is a cloud based migration service providing (to start with) a online migration tool that we migrate Kelvarn Postbox mailboxes (email) with all the settings, attachments from one system to another.Lorem ipsum dolor sit amet, consectetur adipiscing elit, sed do eiusmod tempor incididunt ut labore et dolore magna aliqua.</p>

  <div class="abs feature" style="left:237px">
    <svg width="100" height="70" viewBox="0 0 100 70">
      <rect x="1" y="4" width="98" height="62" fill="#c9c9c9"/>
      <path d="M1 4 L50 42 L99 4" fill="none" stroke="#fff" stroke-width="3"/>
      <path d="M1 66 L40 34 M99 66 L60 34" stroke="#fff" stroke-width="3"/>
    </svg>
    <div class="label">MIGRATING MAIL</div>
  </div>

  <div class="abs feature active" style="left:473px">
    <svg width="100" height="90" viewBox="0 0 100 90">
      <rect x="10" y="18" width="80" height="50" rx="4" fill="none" stroke="#1aa6dc" stroke-width="5"/>
      <rect x="0" y="72" width="100" height="9" rx="4" fill="#1aa6dc"/>
      <path d="M58 8 l14 0 l0 12 l-6 6 l-20 30 l-8 -5 l20 -30 z" fill="#1aa6dc"/>
      <path d="M26 30 l0 20 l5 -5 l5 9 l4 -2 l-5 -9 l7 0 z" fill="#1aa6dc"/>
    </svg>
    <div class="label">REPAIR COURRUPTED DATE</div>
  </div>

  <div class="abs feature" style="left:705px">
    <svg width="100" height="100" viewBox="0 0 100 100">
      <path d="M10 10 L50 0 L80 10 L80 45 C80 70 60 88 40 98 C20 88 5 70 10 45 Z" fill="#cfcfcf"/>
      <path d="M22 20 L50 12 L68 18 L68 45 C68 64 55 78 40 86 C27 78 18 64 22 45 Z" fill="#fff"/>
      <circle cx="72" cy="28" r="22" fill="#bdbdbd"/>
      <path d="M61 28 l8 8 l14 -15" fill="none" stroke="#fff" stroke-width="6"/>
    </svg>
    <div class="label">SECURE</div>
  </div>
</section>

<section>
  <div class="abs benefits"></div>
  <div class="abs benefits-art" role="img" aria-label="Three round icons for cost savings, service and process resilience"></div>
  <span class="abs step-num" style="left:80px;top:1382px">1.</span>
  <span class="abs step-num" style="left:233px;top:1238px">2.</span>
  <span class="abs step-num" style="left:316px;top:1412px">3.</span>

  <h2 class="abs benefits-title">OUR BENEFITS</h2>
  <p class="abs benefits-text">We are therefore developing cloud based migration software/website which will automate the process, mitigating these issues, as well as providing additional benefits such as the ability to sort and migrate only certain areas of data or certain emails.</p>
  <div class="abs benefit-item" style="left:470px;width:140px">1. COST SAVINGS</div>
  <div class="abs benefit-item" style="left:640px;width:200px">2. IMPROVED CUSTOMER SERVICES</div>
  <div class="abs benefit-item" style="left:875px;width:230px">3. IMPROVED RESILIENCE OF THE PROCESS</div>
  <div class="abs outline-btn">Transfer Tortoise's benefits</div>
</section>

<section>
  <h2 class="abs section-title blog-title">OUR BLOG</h2>
  <article class="abs post" style="left:79px">
    <p>Lorem ipsum dolor sit amet, consectetur adipiscing elit, sed do eiusmod tempor.</p>
    <div class="meta">
      <span><svg width="20" height="16" viewBox="0 0 20 16"><path d="M2 1h11a2 2 0 0 1 2 2v6a2 2 0 0 1-2 2H7l-4 3v-3H2a2 2 0 0 1-2-2V3a2 2 0 0 1 2-2z" fill="#1aa6dc"/><path d="M16 5h2a2 2 0 0 1 2 2v5a2 2 0 0 1-2 2v2l-3-2h-4l1-2h3a1 1 0 0 0 1-1z" fill="#1aa6dc"/></svg>1000</span>
      <span><svg width="22" height="14" viewBox="0 0 22 14"><path d="M1 7C4 2 8 0 11 0s7 2 10 7c-3 5-7 7-10 7S4 12 1 7z" fill="#1aa6dc"/><circle cx="11" cy="7" r="3.5" fill="#fff"/><circle cx="11" cy="7" r="2" fill="#1aa6dc"/></svg>12.2500</span>
    </div>
    <a>READ MORE</a>
  </article>
  <article class="abs post" style="left:454px">
    <p>Lorem ipsum dolor sit amet, consectetur adipiscing elit, sed do eiusmod tempor.</p>
    <div class="meta">
      <span><svg width="20" height="16" viewBox="0 0 20 16"><path d="M2 1h11a2 2 0 0 1 2 2v6a2 2 0 0 1-2 2H7l-4 3v-3H2a2 2 0 0 1-2-2V3a2 2 0 0 1 2-2z" fill="#1aa6dc"/><path d="M16 5h2a2 2 0 0 1 2 2v5a2 2 0 0 1-2 2v2l-3-2h-4l1-2h3a1 1 0 0 0 1-1z" fill="#1aa6dc"/></svg>1000</span>
      <span><svg width="22" height="14" viewBox="0 0 22 14"><path d="M1 7C4 2 8 0 11 0s7 2 10 7c-3 5-7 7-10 7S4 12 1 7z" fill="#1aa6dc"/><circle cx="11" cy="7" r="3.5" fill="#fff"/><circle cx="11" cy="7" r="2" fill="#1aa6dc"/></svg>12.2500</span>
    </div>
    <a>READ MORE</a>
  </article>
  <article class="abs post" style="left:829px">
    <p>Lorem ipsum dolor sit amet, consectetur adipiscing elit, sed do eiusmod tempor.</p>
    <div class="meta">
      <span><svg width="20" height="16" viewBox="0 0 20 16"><path d="M2 1h11a2 2 0 0 1 2 2v6a2 2 0 0 1-2 2H7l-4 3v-3H2a2 2 0 0 1-2-2V3a2 2 0 0 1 2-2z" fill="#1aa6dc"/><path d="M16 5h2a2 2 0 0 1 2 2v5a2 2 0 0 1-2 2v2l-3-2h-4l1-2h3a1 1 0 0 0 1-1z" fill="#1aa6dc"/></svg>1000</span>
      <span><svg width="22" height="14" viewBox="0 0 22 14"><path d="M1 7C4 2 8 0 11 0s7 2 10 7c-3 5-7 7-10 7S4 12 1 7z" fill="#1aa6dc"/><circle cx="11" cy="7" r="3.5" fill="#fff"/><circle cx="11" cy="7" r="2" fill="#1aa6dc"/></svg>12.2500</span>
    </div>
    <a>READ MORE</a>
  </article>
</section>

<footer>
  <div class="abs footer"></div>

  <h3 class="abs foot-heading" style="left:79px;top:1935px">Keep In Touch</h3>
  <div class="abs contact-row" style="top:1990px">
    <span class="dot"><svg width="14" height="20" viewBox="0 0 14 20"><path d="M7 0a7 7 0 0 1 7 7c0 5-7 13-7 13S0 12 0 7a7 7 0 0 1 7-7z" fill="#111"/><circle cx="7" cy="7" r="2.5" fill="#fff"/></svg></span>
    <span>Lorem ipsum dolor sit amet, consectetur adipiscing elit,</span>
  </div>
  <div class="abs contact-row" style="top:2054px">
    <span class="dot"><svg width="12" height="20" viewBox="0 0 12 20"><rect x="0" y="0" width="12" height="20" rx="2" fill="#111"/><rect x="2" y="3" width="8" height="11" fill="#fff"/><circle cx="6" cy="17" r="1.2" fill="#fff"/></svg></span>
    <span>+01234567890</span>
  </div>
  <div class="abs contact-row" style="top:2119px">
    <span class="dot"><svg width="16" height="12" viewBox="0 0 16 12"><rect width="16" height="12" rx="1" fill="#111"/><path d="M0 1l8 6 8-6" fill="none" stroke="#fff" stroke-width="1.5"/></svg></span>
    <span>xyz@example.com</span>
  </div>

  <h3 class="abs connect-title">Get Connect with US</h3>
  <div class="abs field" style="left:391px;top:2001px;width:417px;height:31px">NAME</div>
  <div class="abs field" style="left:391px;top:2035px;width:417px;height:33px">EMAIL ID</div>
  <div class="abs field" style="left:391px;top:2071px;width:313px;height:84px">MESSAGE</div>
  <div class="abs send-btn">SEND</div>
  <div class="abs social" style="left:538px"><i></i></div>
  <div class="abs social" style="left:569px"><i></i></div>
  <div class="abs social" style="left:600px"><i></i></div>
  <div class="abs social" style="left:631px"><i></i></div>

  <h3 class="abs foot-heading" style="left:880px;top:1935px">More Information</h3>
  <p class="abs more-text">Lorem ipsum dolor sit amet, consectetur adipiscing elit, sed do eiusmod tempor incididunt ut labore et dolore magna aliqua.</p>
  <a class="abs know-more">KNOW MORE</a>

  <div class="abs rule"></div>
  <div class="abs to-top"><svg width="22" height="20" viewBox="0 0 22 20"><path d="M3 10l8-7 8 7M3 17l8-7 8 7" fill="none" stroke="#fff" stroke-width="3"/></svg></div>
  <p class="abs copyright">© <b>Transfer Tortoise</b> - 2016. All Rights Reserved.</p>
</footer>

</body>
</html>
```